www.brightlingua.example -- International Language school needs a Wordpress Design

NOTE: This is for a complete WordPress website with coding (Design/develop)

We are a small, private English language school in business for 15 years. Our students come from around the world to study English at our centre in Toronto, Canada. Most of our students are in their 20's and come to study English with us for periods of 1-6 months before returning home to complete their post-secondary education or pursue their careers.

We are looking for a talented web designer to redevelop our sadly outdated website (www.brightlingua.example) to bring a fresh look with vastly increased functionality and web traffic.

Target Market(s)

-20s and 30s; mostly upper-middle class, educated
-from non-English speaking countries, but often have some English background
-looking to improve their English (mostly speaking) skills at our school like ours and experience living in a new country (like exchange students)

Industry/Entity Type

Education

Font styles to use
Sans Serif

Requirements
Must have
• - page listing our programs
- page with our fees and starting dates
- application form
- page showing why BRIGHT (us)?
- page with accommodation options
* responsive design
Nice to have
• examples of other websites in our industry I like:

http://www.maryholt.example/
http://www.tqlearn.example/en
http://en.rpz.example/
http://www.harrowgate-college.example/

```html
<!DOCTYPE html>
<html lang="en">
<head>
<meta charset="utf-8">
<title>Bright English School</title>
<link href="https://fonts.googleapis.com/css2?family=Open+Sans:wght@300;400;600;700&display=swap" rel="stylesheet">
<style>
:root{
  --orange:#ef8f0b;
  --orange-dark:#d97d00;
  --topbar:#3f3f3f;
  --band:#2d2d2d;
  --green:#1b8f68;
  --dark:#2a2a2a;
  --footer:#f3f3f3;
  --text:#666;
  --light:#fff;
  --line:#dedede;
}
*{box-sizing:border-box;margin:0;padding:0}
html,body{width:1200px;height:2345px;overflow:hidden}
body{position:relative;font-family:"Open Sans",Arial,sans-serif;color:var(--text);background:#fff}
section,header,footer,div.abs{position:absolute;left:0;width:1200px}

/* top bar */
.topbar{top:0;height:38px;background:var(--topbar);color:#eee;font-size:11px;display:flex;align-items:center;padding:0 68px}
.topbar .info{display:flex;gap:26px;align-items:center}
.topbar .info span{display:flex;align-items:center;gap:6px}
.topbar .links{margin-left:40px;display:flex;gap:20px}
.topbar .social{margin-left:auto;display:flex;gap:6px}
.topbar .social i{width:22px;height:22px;border:1.5px solid var(--orange);border-radius:50%;display:block}

/* header */
.header{top:38px;height:99px;background:rgba(239,143,11,.93);z-index:3;display:flex;align-items:center;padding:0 68px 0 72px}
.brand{display:flex;align-items:center;gap:10px;font-size:38px;font-weight:700;color:#1e1e1e;letter-spacing:.5px}
.brand i{width:30px;height:30px;border-radius:50%;background:#1e1e1e;display:block}
.nav{margin-left:auto;display:flex;gap:16px;font-size:14px;color:#fff;text-transform:uppercase}
.nav a{color:#fff;text-decoration:none}
.nav a.current{color:#222;border-bottom:2px solid #222;padding-bottom:4px}

/* hero */
.hero{top:38px;height:456px;overflow:hidden}
.hero .main{position:absolute;left:0;top:0;width:720px;height:456px;background:linear-gradient(110deg,#6b4a2c 0%,#c89a6a 35%,#e0b27a 50%,#7b5434 75%,#3d2a1b 100%)}
.hero .tile{position:absolute}
.hero .t1{left:720px;top:99px;width:245px;height:168px;background:linear-gradient(160deg,#7ea0c0,#9d8a70 60%,#5a5048)}
.hero .t2{left:967px;top:99px;width:233px;height:168px;background:linear-gradient(160deg,#cfc6bc,#8a7466 60%,#4f4038)}
.hero .t3{left:720px;top:269px;width:480px;height:160px;background:linear-gradient(120deg,#6d5a4e,#b8675a 40%,#e0d2c6 60%,#7a6254)}
.hero .fade{position:absolute;left:0;bottom:0;width:1200px;height:32px;background:linear-gradient(rgba(255,255,255,0),rgba(255,255,255,.75))}

/* program band */
.programs{top:494px;height:157px;background:var(--band);display:flex;padding:8px 0 0 67px;gap:0}
.program{width:279px;text-align:center;color:#fff}
.program h3{font-weight:300;font-size:32px;line-height:36px;margin-top:4px}
.program p{font-size:12px;font-weight:600;margin-top:8px;font-family:Arial,sans-serif}
.program.active{width:243px;height:101px;background:var(--orange);margin-right:36px}
.program.active h3{margin-top:2px}
.program.active p{margin-top:6px}

/* intro */
.intro{top:651px;height:486px}
.intro h2{position:absolute;left:67px;top:36px;font-size:20px;font-weight:400;color:#333}
.tabs{position:absolute;left:67px;top:71px;width:706px;height:378px;border:1px solid var(--line);border-radius:3px}
.tabs ul{list-style:none;display:flex;height:36px;border-bottom:1px solid var(--line);font-size:13px}
.tabs li{padding:0 14px;line-height:36px;color:#555;border-right:1px solid var(--line)}
.tabs li.on{color:var(--orange)}
.tabs .photos{position:absolute;left:19px;top:58px;width:668px;height:182px;display:flex;gap:2px}
.tabs .photos div{flex:1}
.tabs .p1{background:linear-gradient(135deg,#8a6a50,#c66a4e 40%,#6a7fa8 70%,#5a4a3e)}
.tabs .p2{background:linear-gradient(135deg,#b9b3aa,#3a2f2c 40%,#2f63b6 70%,#cfc8c0)}
.tabs .copy{position:absolute;left:19px;top:246px;width:668px;font-size:12px;line-height:19px;font-family:Arial,sans-serif;color:#777}
.tabs .copy b{color:#555}

.contact{position:absolute;left:809px;top:36px;width:334px}
.contact h2{position:static;font-size:20px;font-weight:400;color:#333}
.fields{margin-top:15px;border:1px solid var(--line);border-radius:3px}
.field{height:35px;border-bottom:1px solid var(--line);font-size:12px;line-height:35px;padding:0 10px;color:#888;display:flex;justify-content:space-between;align-items:center}
.field:last-child{border-bottom:0}
.message{margin-top:14px;height:135px;border:1px solid var(--line);border-radius:3px;padding:10px;font-size:12px;color:#888}
.actions{margin-top:17px;display:flex;justify-content:space-between;align-items:center}
.btn{background:var(--orange-dark);color:#fff;font-size:12px;padding:0 10px;height:31px;line-height:31px;border-radius:3px}
.clear{font-size:11px;color:var(--orange);display:flex;align-items:center;gap:4px}

/* student corner */
.corner{top:1137px;height:317px;background:var(--green);color:#fff}
.corner h2{text-align:center;font-size:41px;font-weight:300;margin-top:30px}
.corner .up{position:absolute;right:8px;top:54px;width:26px;height:26px;border-radius:50%;background:rgba(255,255,255,.25)}
.features{position:absolute;left:50px;top:100px;width:1100px;display:flex}
.feature{width:275px;height:180px;text-align:center;border-right:1px solid rgba(255,255,255,.45);padding:0 25px}
.feature:last-child{border-right:0}
.feature .icon{height:50px;margin-top:10px;display:flex;align-items:center;justify-content:center}
.feature h4{font-size:19px;font-weight:400;color:#11342a;margin-top:6px;line-height:24px}
.feature p{font-family:Arial,sans-serif;font-size:13px;line-height:20px;margin-top:4px}

/* testimonials + gallery */
.voices{top:1454px;height:531px;background:var(--dark);color:#fff}
.voices h2{text-align:center;font-size:28px;font-weight:300;margin-top:33px}
.quote{position:absolute;left:33px;top:87px;width:1146px;height:159px;border:1px solid #888;border-radius:3px;padding:16px 28px 0}
.quote p{text-align:center;font-size:17.5px;font-weight:600;line-height:25px}
.who{position:absolute;left:15px;bottom:14px;display:flex;align-items:center;gap:14px;font-size:13px;color:#555}
.who i{width:38px;height:38px;border-radius:50%;background:#c9c2b8;display:block}
.marker{position:absolute;left:0;top:208px;width:12px;height:62px;background:var(--orange)}
.dots{position:absolute;left:0;top:252px;width:1200px;text-align:center;color:#aaa;font-size:14px;letter-spacing:2px}
.voices h3{position:absolute;top:270px;width:1200px;text-align:center;font-size:28px;font-weight:300}
.gallery{position:absolute;left:33px;top:322px;display:flex;gap:16px;width:1167px;overflow:hidden}
.gallery div{flex:0 0 242px;height:170px}
.g1{background:linear-gradient(#b7c6d2,#e6eaee 55%,#9aa4ad)}
.g2{background:linear-gradient(135deg,#f0ebe4,#4a3a22 45%,#d8a78a 70%,#fff)}
.g3{background:linear-gradient(135deg,#b9b9b9,#383838 40%,#a06a50 65%,#d8d0c8)}
.g4{background:linear-gradient(135deg,#e3dfda,#5a4a40 40%,#b89a7c 70%,#efe9e3)}
.g5{background:linear-gradient(135deg,#d9d3cc,#6a4a3a 50%,#c0b6aa)}
.next{position:absolute;right:12px;top:378px;width:22px;height:44px;background:var(--orange);border-radius:3px}

/* footer */
.footer{top:1985px;height:292px;background:var(--footer);border-top:1px solid #ddd}
.col{position:absolute;top:38px;width:220px}
.col h5{font-size:14px;font-weight:400;color:#444;text-transform:uppercase}
.col ul{list-style:none;margin-top:16px;font-size:11.5px;line-height:17px;font-family:Arial,sans-serif;color:#888}
.c1{left:120px}.c2{left:370px}.c3{left:620px}.c4{left:869px}
.post{display:flex;gap:14px;margin-top:16px}
.post i{width:52px;height:52px;border:1px solid #ddd;border-radius:50%;display:block}
.post span{font-size:11.5px;color:#888;line-height:17px;font-family:Arial,sans-serif}
.post small{display:block;color:#444;font-size:10px}
.thumbs{margin-top:16px;display:grid;grid-template-columns:repeat(4,52px);gap:3px}
.thumbs div{height:52px}
.thumbs div:nth-child(1){background:#8a4a44}.thumbs div:nth-child(2){background:#5d6270}
.thumbs div:nth-child(3){background:#4f6a3e}.thumbs div:nth-child(4){background:#6a5a58}
.thumbs div:nth-child(5){background:#7a8aa0}.thumbs div:nth-child(6){background:#4a4f5a}
.bottom{top:2277px;height:68px;background:#fff;border-top:1px solid #e3e3e3;display:flex;align-items:center;padding-left:124px;gap:36px}
.bottom .brand{font-size:30px}
.bottom .brand i{width:24px;height:24px}
.bottom small{font-size:9px;color:#777}
.totop{position:absolute;right:10px;bottom:6px;width:22px;height:22px;border-radius:50%;background:#e6a55a}
</style>
</head>
<body>

<div class="abs topbar">
  <div class="info">
    <span><svg width="9" height="12" viewBox="0 0 9 12"><path d="M4.5 0A4.5 4.5 0 0 0 0 4.5C0 8 4.5 12 4.5 12S9 8 9 4.5A4.5 4.5 0 0 0 4.5 0Z" fill="#ddd"/><circle cx="4.5" cy="4.5" r="1.6" fill="#3f3f3f"/></svg>48 Harbour Lane, Suite 12 Toronto, Ontario M5X 1Z9 Canada</span>
    <span><svg width="8" height="12" viewBox="0 0 8 12"><rect x="1" y="0" width="6" height="12" rx="1" fill="#ddd"/></svg>+1-555-014-2290</span>
    <span><svg width="12" height="9" viewBox="0 0 12 9"><rect width="12" height="9" rx="1" fill="#ddd"/><path d="M0 0L6 5L12 0" stroke="#3f3f3f" fill="none"/></svg>info@brightlingua.example</span>
    <span><svg width="11" height="11" viewBox="0 0 11 11"><circle cx="5.5" cy="5.5" r="4.8" stroke="#ddd" fill="none" stroke-width="1.3"/><path d="M5.5 2.5V5.5H8" stroke="#ddd" fill="none"/></svg>9am -4pm</span>
  </div>
  <div class="links"><span>News</span><span>Agent</span></div>
  <div class="social"><i></i><i></i><i></i><i></i><i></i></div>
</div>

<header class="header">
  <div class="brand"><i></i>bright</div>
  <nav class="nav">
    <a class="current">Home</a><a>Our School ▾</a><a>Programs ▾</a><a>Fees &amp; Dates ▾</a><a>Accommodation ▾</a><a>Students Corner ▾</a>
  </nav>
</header>

<section class="hero">
  <div class="main" role="img" aria-label="Smiling students sitting together in class"></div>
  <div class="tile t1" role="img" aria-label="Toronto city skyline with the tower"></div>
  <div class="tile t2" role="img" aria-label="Students studying at a table"></div>
  <div class="tile t3" role="img" aria-label="Group of students at a holiday party"></div>
  <div class="fade"></div>
</section>

<section class="programs">
  <div class="program active"><h3>ENGLISH<br>COURSES</h3><p>find our our all programs</p></div>
  <div class="program"><h3>Full-Time<br>Programs</h3><p>Intensive Focus</p></div>
  <div class="program"><h3>Bright Junior<br>Programs</h3><p>Parent &amp; Child</p></div>
  <div class="program"><h3>Special<br>Programs</h3><p>University Bridge</p></div>
</section>

<section class="intro">
  <h2>Learn English from expert. Join Bright today</h2>
  <div class="tabs">
    <ul><li class="on">About us</li><li>Why Bright ?</li><li>Our Features</li><li>F A Q</li><li>Apply Online</li></ul>
    <div class="photos">
      <div class="p1" role="img" aria-label="Students working around a classroom table"></div>
      <div class="p2" role="img" aria-label="Two students posing in the school lounge"></div>
    </div>
    <p class="copy"><b>Lorem Ipsum</b> is simply dummy text of the printing and typesetting industry. Lorem Ipsum has been the industry's standard dummy text ever since the 1500s, when an unknown printer took a galley of type and scrambled it to make a type specimen book. It has survived not only five centuries, but also the leap into electronic typesetting, remaining essentially unchanged. It was popularised in the 1960s with the release of Typemark sheets containing Lorem Ipsum passages, and more recently with desktop publishing software like Quillset Layout including versions of Lorem Ipsum.</p>
  </div>
  <div class="contact">
    <h2>Get in touch with Bright</h2>
    <div class="fields">
      <div class="field">Name *<span>⚲</span></div>
      <div class="field">E-mail *<span>✉</span></div>
      <div class="field">Telephone<span>✆</span></div>
      <div class="field">Country<span>⌖</span></div>
    </div>
    <div class="message">Message *</div>
    <div class="actions"><span class="btn">Send message</span><span class="clear">clear ⊗</span></div>
  </div>
</section>

<section class="corner">
  <h2>Student Corner</h2>
  <i class="up"></i>
  <div class="features">
    <div class="feature">
      <div class="icon"><svg width="50" height="40" viewBox="0 0 50 40"><path d="M2 14h8l14-10v32L10 26H2z" fill="var(--orange)"/><path d="M30 12q6 8 0 16M36 7q10 13 0 26M42 2q14 18 0 36" stroke="var(--orange)" stroke-width="3" fill="none"/></svg></div>
      <h4>News &amp; Events</h4>
      <p>simply dummy text of the printing and typesetting industry. Lorem Ipsum has been the industry's standard dummy text ever since the 1500s,</p>
    </div>
    <div class="feature">
      <div class="icon"><svg width="40" height="42" viewBox="0 0 40 42"><path d="M8 2h28l-6 32H2z" fill="var(--orange)"/><path d="M2 34h28l-2 6H0z" fill="none" stroke="var(--orange)" stroke-width="2.5"/><path d="M12 10h16M11 16h16" stroke="var(--green)" stroke-width="2"/></svg></div>
      <h4>Lessons</h4>
      <p>simply dummy text of the printing and typesetting industry. Lorem Ipsum has been the industry's standard dummy text ever since the 1500s,</p>
    </div>
    <div class="feature">
      <div class="icon"><svg width="46" height="40" viewBox="0 0 46 40"><rect x="1.5" y="6" width="43" height="32" rx="4" fill="none" stroke="var(--orange)" stroke-width="3"/><rect x="6" y="1" width="10" height="6" fill="var(--orange)"/><circle cx="23" cy="22" r="9" fill="none" stroke="var(--orange)" stroke-width="3"/><circle cx="23" cy="22" r="4" fill="var(--orange)"/></svg></div>
      <h4>Photo Gallery</h4>
      <p>simply dummy text of the printing and typesetting industry. Lorem Ipsum has been the industry's standard dummy text ever since the 1500s,</p>
    </div>
    <div class="feature">
      <div class="icon"><svg width="42" height="42" viewBox="0 0 42 42"><rect x="2" y="18" width="8" height="22" fill="none" stroke="var(--orange)" stroke-width="3"/><path d="M13 18L22 3q5 0 4 6l-2 8h12q5 1 4 6l-3 14q-1 3-4 3H13z" fill="none" stroke="var(--orange)" stroke-width="3"/></svg></div>
      <h4>Meet our students</h4>
      <p>simply dummy text of the printing and typesetting industry. Lorem Ipsum has been the industry's standard dummy text ever since the 1500s,</p>
    </div>
  </div>
</section>

<section class="voices">
  <h2>What our students says about Bright English School</h2>
  <div class="quote">
    <p>Lorem Ipsum is simply dummy text of the printing and typesetting industry. Lorem Ipsum has been the industry's standard dummy text ever since the 1500s, when an unknown printer took a galley of type and scrambled it to make a type specimen book. It has survived not only five centuries, but also the leap into electronic typesetting, remaining essentially unchanged.</p>
    <div class="who"><i role="img" aria-label="Student portrait"></i>Daniel Kim – Korea</div>
  </div>
  <i class="marker"></i>
  <div class="dots">• • •</div>
  <h3>Students Gallery</h3>
  <div class="gallery">
    <div class="g1" role="img" aria-label="Students ice skating outdoors"></div>
    <div class="g2" role="img" aria-label="Friends sharing a meal"></div>
    <div class="g3" role="img" aria-label="Students in holiday hats giving a thumbs up"></div>
    <div class="g4" role="img" aria-label="Students building a gingerbread house"></div>
    <div class="g5" role="img" aria-label="Students at a holiday gathering"></div>
  </div>
  <i class="next"></i>
</section>

<footer class="footer">
  <div class="col c1"><h5>Knowledgebase</h5>
    <ul><li>Tips &amp; Tricks</li><li>Downloads</li><li>Articles and Magazines</li><li>Learn from the beginning</li><li>Tips &amp; Tricks</li><li>Downloads</li><li>Articles and Magazines</li><li>Learn from the beginning</li></ul></div>
  <div class="col c2"><h5>News &amp; Blogs</h5>
    <div class="post"><i></i><span>Hello world!<small>February 7, 2015</small></span></div></div>
  <div class="col c3"><h5>Gallery</h5>
    <div class="thumbs" role="img" aria-label="Small student photo thumbnails"><div></div><div></div><div></div><div></div><div></div><div></div></div></div>
  <div class="col c4"><h5>Help Desk</h5>
    <ul><li>Student Forum</li><li>Course Enquiry</li><li>Classes and Time</li><li>Fees details</li><li>Apply online</li></ul></div>
</footer>

<div class="abs bottom">
  <div class="brand"><i></i>bright</div>
  <small>Powered By : lumenweb</small>
  <i class="totop"></i>
</div>

</body>
</html>
```